Brantomere Promotional Flier

1 page flier that can be emailed to perspective customers or printed and distributed. Flier should use logo and design cues from our website, brantomere-example.com. We offer equipment financing and business loans to small businesses. The design should incorporate the highlights of working with Brantomere which include:

Benefits:
- Approvals In Hours
- Automated, Easy Application Process
- New and Used Equipment Financed
- 92% Approval Rate
-Flexible Terms
- Superior Support

Program Minimums:
- 450 Minimum Credit Score
- 2 months minimum Time In Business
- $7,500/mo minimum revenue deposits

Target Market(s)

Small To Medium Sized businesses

Industry/Entity Type

Finance

Font styles to use
Sans Serif

Colors
0555a3
3075b4
85acd3
cfdeed

Requirements
Should not have
• No cheesy money bags or dollar signs fling aorund. Should be professional

```html
<!DOCTYPE html>
<html lang="en">
<head>
<meta charset="utf-8">
<title>Brantomere Promotional Flier</title>
<link rel="stylesheet" href="https://fonts.googleapis.com/css2?family=Montserrat:wght@300;400;600;700;800&family=Varela+Round&display=swap">
<style>
:root{
  --blue-deep:#0555a3;
  --blue-mid:#3075b4;
  --blue-soft:#85acd3;
  --blue-pale:#cfdeed;
  --ink:#1a1a1a;
  --white:#ffffff;
  --grey-stripe:#e6e6e6;
  --panel-bg:#f7f8fa;
}
*{margin:0;padding:0;box-sizing:border-box}
html,body{width:961px;height:1200px;overflow:hidden;background:var(--white)}
.flier{position:relative;width:961px;height:1200px;overflow:hidden;font-family:"Montserrat",sans-serif;background:var(--white)}

/* header */
.header{position:absolute;left:0;top:0;width:961px;height:180px;background:var(--white)}
.header-shapes{position:absolute;left:0;top:0}
.brand-name{position:absolute;left:92px;top:62px;font-weight:600;font-size:66px;color:var(--blue-deep);letter-spacing:-1px;line-height:1}
.website{position:absolute;left:646px;top:112px;display:flex;align-items:center;gap:12px;color:var(--white);font-weight:400;font-size:20px;white-space:nowrap}
.website b{font-weight:600}

/* hero */
.hero-photo{position:absolute;left:0;top:180px;width:961px;height:454px;background:linear-gradient(160deg,#1c3b6b 0%,#14305c 45%,#0c2146 100%)}
.hero-rule{position:absolute;left:108px;top:246px;width:5px;height:154px;background:var(--white)}
.hero-title{position:absolute;left:145px;top:250px;font-size:58px;color:var(--white);font-weight:300;letter-spacing:-1px;white-space:nowrap;line-height:1}
.hero-title strong{font-weight:800;letter-spacing:0}
.hero-sub{position:absolute;left:148px;top:326px;font-size:25px;font-weight:300;color:var(--white);line-height:38px}

/* band */
.include-band{position:absolute;left:0;top:634px;width:961px;height:79px;background:var(--blue-deep);display:flex;align-items:center;justify-content:center}
.include-band h2{font-size:32px;font-weight:800;color:var(--white);letter-spacing:.3px;white-space:nowrap}

/* content */
.content{position:absolute;left:0;top:713px;width:961px;height:421px;background:linear-gradient(135deg,#f4f5f7 0%,#ffffff 55%,#f1f3f6 100%)}
.panel{position:absolute;border:2px solid var(--blue-mid);border-radius:10px}
.panel-title{position:absolute;top:-22px;z-index:2;background:var(--panel-bg);font-weight:800;color:var(--blue-deep);padding:0 12px;line-height:40px;white-space:nowrap}
.benefits{left:67px;top:32px;width:384px;height:369px}
.benefits .panel-title{left:82px;font-size:32px}
.minimums{left:480px;top:32px;width:432px;height:369px}
.minimums .panel-title{left:24px;font-size:29px}

.benefit-list{list-style:none}
.benefit{position:absolute;left:0;width:100%;height:60px;display:flex;align-items:center}
.benefit-icon{flex:none;width:40px;height:40px;margin-left:30px}
.benefit-divider{flex:none;width:2px;margin-left:22px;background:var(--blue-mid)}
.benefit-divider.single{height:36px}
.benefit-divider.double{height:58px}
.benefit-text{margin-left:20px;font-family:"Varela Round",sans-serif;font-size:20.5px;color:var(--ink);line-height:27px;white-space:nowrap}

.minimum{position:absolute;left:38px;display:flex;align-items:center}
.minimum-badge{flex:none;width:80px;height:80px;border-radius:50%;background:var(--blue-deep);display:flex;align-items:center;justify-content:center;box-shadow:0 0 0 3px var(--blue-pale)}
.minimum-text{margin-left:18px;font-family:"Varela Round",sans-serif;font-size:24px;line-height:30px;color:var(--ink);white-space:nowrap}
.minimum-text em{font-style:normal;color:var(--blue-deep);font-weight:700;font-family:"Montserrat",sans-serif}

/* footer */
.footer{position:absolute;left:0;top:1134px;width:961px;height:66px;background:var(--blue-mid)}
.footer-shape{position:absolute;left:0;top:0}
.contact{position:absolute;top:0;height:66px;display:flex;align-items:center;gap:10px;color:var(--white);font-family:"Varela Round",sans-serif;font-size:21px;white-space:nowrap}
.contact.phone{left:66px}
.contact.fax{left:368px}
.contact.email{left:624px;font-size:19px}
</style>
</head>
<body>
<div class="flier">

  <header class="header">
    <svg class="header-shapes" width="961" height="180" viewBox="0 0 961 180">
      <polygon points="617,0 667,0 587,180 537,180" fill="var(--grey-stripe)"/>
      <polygon points="667,0 961,0 961,180 587,180" fill="var(--blue-deep)"/>
    </svg>
    <div class="brand-name">Brantomere</div>
    <div class="website">
      <svg width="20" height="20" viewBox="0 0 20 20" fill="none" stroke="#fff" stroke-width="1.6">
        <circle cx="10" cy="10" r="8.5"/><ellipse cx="10" cy="10" rx="3.8" ry="8.5"/><line x1="1.5" y1="10" x2="18.5" y2="10"/>
      </svg>
      <span><b>brantomere-example</b>.com</span>
    </div>
  </header>

  <div class="hero-photo" role="img" aria-label="Photo looking up at tall glass office towers, tinted dark blue"></div>
  <div class="hero-rule"></div>
  <h1 class="hero-title">FAST. EASY. <strong>FINANCING</strong></h1>
  <p class="hero-sub">We offer equipment financing<br>and business loans to small businesses.</p>

  <div class="include-band">
    <h2>WORKING WITH Brantomere WHICH INCLUDE:</h2>
  </div>

  <section class="content">
    <div class="panel benefits">
      <h3 class="panel-title">BENEFITS:</h3>
      <ul class="benefit-list">
        <li class="benefit" style="top:18px">
          <svg class="benefit-icon" viewBox="0 0 40 40" fill="none" stroke="var(--blue-deep)" stroke-width="2"><circle cx="20" cy="20" r="16"/><polyline points="20,10 20,20 27,20"/></svg>
          <span class="benefit-divider single"></span>
          <span class="benefit-text">Approvals In Hours</span>
        </li>
        <li class="benefit" style="top:78px">
          <svg class="benefit-icon" viewBox="0 0 40 40" fill="none" stroke="var(--blue-deep)" stroke-width="2"><rect x="4" y="8" width="16" height="26"/><rect x="18" y="4" width="18" height="30"/><line x1="22" y1="22" x2="32" y2="22"/><line x1="22" y1="27" x2="32" y2="27"/><circle cx="27" cy="13" r="3"/></svg>
          <span class="benefit-divider double"></span>
          <span class="benefit-text">Automated, Easy<br>Application Process</span>
        </li>
        <li class="benefit" style="top:144px">
          <svg class="benefit-icon" viewBox="0 0 40 40" fill="none" stroke="var(--blue-deep)" stroke-width="2"><polygon points="4,12 20,4 36,12"/><rect x="6" y="12" width="28" height="20"/><circle cx="20" cy="22" r="6"/><line x1="3" y1="35" x2="37" y2="35"/></svg>
          <span class="benefit-divider double"></span>
          <span class="benefit-text">New and Used<br>Equipment Financed</span>
        </li>
        <li class="benefit" style="top:197px">
          <svg class="benefit-icon" viewBox="0 0 40 40" fill="none" stroke="var(--blue-deep)" stroke-width="2"><rect x="6" y="8" width="22" height="28"/><line x1="10" y1="15" x2="24" y2="15"/><line x1="10" y1="20" x2="20" y2="20"/><circle cx="15" cy="28" r="4"/><line x1="24" y1="20" x2="36" y2="6"/></svg>
          <span class="benefit-divider single"></span>
          <span class="benefit-text">92% Approval Rate</span>
        </li>
        <li class="benefit" style="top:249px">
          <svg class="benefit-icon" viewBox="0 0 40 40" fill="none" stroke="var(--blue-deep)" stroke-width="2"><rect x="7" y="3" width="22" height="32"/><line x1="11" y1="10" x2="25" y2="10"/><line x1="11" y1="15" x2="25" y2="15"/><line x1="11" y1="20" x2="21" y2="20"/><circle cx="30" cy="31" r="6"/><polyline points="27,31 29.5,33.5 33,29"/></svg>
          <span class="benefit-divider single"></span>
          <span class="benefit-text">Flexible Terms</span>
        </li>
        <li class="benefit" style="top:297px">
          <svg class="benefit-icon" viewBox="0 0 40 40" fill="none" stroke="var(--blue-deep)" stroke-width="2"><circle cx="20" cy="13" r="8"/><path d="M10 13a10 10 0 0 1 20 0"/><path d="M5 38c0-9 7-13 15-13s15 4 15 13z"/></svg>
          <span class="benefit-divider single"></span>
          <span class="benefit-text">Superior Support</span>
        </li>
      </ul>
    </div>

    <div class="panel minimums">
      <h3 class="panel-title">PROGRAM MINIMUMS:</h3>
      <div class="minimum" style="top:45px">
        <div class="minimum-badge">
          <svg width="50" height="50" viewBox="0 0 50 50" fill="none" stroke="#fff" stroke-width="2"><circle cx="25" cy="25" r="20"/><path d="M11 32a15 15 0 1 1 28 0"/><line x1="25" y1="30" x2="25" y2="14"/><circle cx="25" cy="31" r="3"/></svg>
        </div>
        <p class="minimum-text"><em>450</em> Minimum<br>Credit Score</p>
      </div>
      <div class="minimum" style="top:148px">
        <div class="minimum-badge">
          <svg width="48" height="48" viewBox="0 0 48 48" fill="none" stroke="#fff" stroke-width="2"><rect x="6" y="9" width="36" height="32" rx="3"/><line x1="6" y1="17" x2="42" y2="17"/><line x1="15" y1="5" x2="15" y2="12"/><line x1="33" y1="5" x2="33" y2="12"/><circle cx="15" cy="25" r="2.5"/><circle cx="24" cy="25" r="2.5"/><circle cx="33" cy="25" r="2.5"/><circle cx="15" cy="33" r="3.5"/><circle cx="24" cy="33" r="3.5"/></svg>
        </div>
        <p class="minimum-text"><em>2 months</em> minimum<br>Time In Business</p>
      </div>
      <div class="minimum" style="top:254px">
        <div class="minimum-badge">
          <svg width="50" height="50" viewBox="0 0 50 50" fill="none" stroke="#fff" stroke-width="2"><rect x="14" y="26" width="26" height="14" rx="2"/><line x1="14" y1="33" x2="40" y2="33"/><path d="M30 8l8 3v6c0 5-4 8-8 9-4-1-8-4-8-9v-6z"/><line x1="4" y1="28" x2="11" y2="28"/><line x1="6" y1="34" x2="11" y2="34"/></svg>
        </div>
        <p class="minimum-text"><em>$7,500/mo</em> minimum<br>revenue deposits</p>
      </div>
    </div>
  </section>

  <footer class="footer">
    <svg class="footer-shape" width="961" height="66" viewBox="0 0 961 66">
      <polygon points="313,0 581,0 615,66 348,66" fill="var(--blue-deep)"/>
    </svg>
    <div class="contact phone">
      <svg width="22" height="22" viewBox="0 0 22 22" fill="none" stroke="#fff" stroke-width="1.6"><circle cx="11" cy="11" r="10"/><path d="M7 6l2 0 1 3-1.5 1a6 6 0 0 0 3.5 3.5L13 12l3 1v2a1 1 0 0 1-1 1A10 10 0 0 1 6 7a1 1 0 0 1 1-1z"/></svg>
      <span>(800) 555-0147</span>
    </div>
    <div class="contact fax">
      <svg width="22" height="20" viewBox="0 0 22 20" fill="#fff"><rect x="5" y="1" width="12" height="5"/><rect x="1" y="7" width="20" height="8" rx="1"/><rect x="5" y="13" width="12" height="6" fill="#fff" stroke="var(--blue-deep)" stroke-width="1"/></svg>
      <span>(310) 555-0192</span>
    </div>
    <div class="contact email">
      <svg width="26" height="18" viewBox="0 0 26 18" fill="none" stroke="#fff" stroke-width="1.6"><rect x="1" y="1" width="24" height="16"/><polyline points="1,1 13,10 25,1"/></svg>
      <span>Info@brantomere-example.com</span>
    </div>
  </footer>

</div>
</body>
</html>
```